Marta Belle Designs & Events business card

I need an elegant informative but not busy business card using my logo. We are a florist with high end customers. I am adding a PDF file and a PNG file for those who requested it
Updates

Target Market(s)

Brides, grooms, men purchasing flowers
Ages 20-65

Industry/Entity Type

Florist

Requirements
Must have
• Business info:
Marta Belle Design & Events
www.martabelleevents-sample.com.
555-418-2763

555-418-2763
Nice to have
• Est 1954
may want Pinterest logo, twitter and linkedin and facbook
Should not have
• Clip art or photos

```html
<!DOCTYPE html>
<html lang="en">
<head>
<meta charset="utf-8">
<title>Marta Belle Designs &amp; Events – Business Cards</title>
<link rel="stylesheet" href="https://fonts.googleapis.com/css2?family=Cinzel:wght@400&family=Cormorant+SC:wght@500&family=Lato:wght@400&display=swap">
<style>
  :root {
    --backdrop: #d6d6d6;
    --paper: #ffffff;
    --ink: #1c1c1c;
    --blush: #eeaabb;
    --blush-soft: #fbe6ec;
    --blush-pale: #fdf3f6;
    --night: #0b0b0b;
    --night-soft: #222222;
    --smoke: #3a3a3a;
    --light-text: #f4f4f4;
  }
  * { margin: 0; padding: 0; box-sizing: border-box; }
  html, body {
    width: 784px; height: 1200px; overflow: hidden;
    background: var(--backdrop);
  }
  .sheet { position: relative; width: 784px; height: 1200px; }

  .card {
    position: absolute;
    width: 500px; height: 286px;
    border-radius: 3px;
    overflow: hidden;
    box-shadow: 0 2px 6px rgba(0,0,0,0.18);
  }
  .card--light { background: var(--paper); color: var(--ink); }
  .card--dark { background: var(--night); color: var(--light-text); }

  .card--front-light { left: 40px; top: 30px; }
  .card--back-light  { left: 244px; top: 326px; }
  .card--front-dark  { left: 40px; top: 630px; }
  .card--back-dark   { left: 244px; top: 906px; }

  /* decorative swirl area on fronts */
  .swirl-field {
    position: absolute; left: 0; top: 0;
    width: 300px; height: 286px;
  }
  .card--light .swirl-field {
    background: radial-gradient(ellipse at 40% 55%, var(--blush-soft) 0%, var(--blush-pale) 55%, var(--paper) 100%);
  }
  .card--dark .swirl-field {
    background: radial-gradient(ellipse at 40% 55%, var(--night-soft) 0%, #151515 55%, var(--night) 100%);
  }

  /* brand lockup */
  .brand {
    position: absolute; left: 40px; top: 150px;
    width: 230px; text-align: center;
  }
  .brand__mark {
    display: block; margin: 0 auto 12px;
    width: 22px; height: 22px; border-radius: 50%;
  }
  .card--light .brand__mark { background: var(--blush); }
  .card--dark .brand__mark { background: var(--blush); }
  .brand__name {
    font-family: "Cinzel", serif;
    font-size: 24px; letter-spacing: 4px; font-weight: 400;
  }
  .card--light .brand__name { color: var(--ink); }
  .card--dark .brand__name { color: var(--light-text); }
  .brand__tagline {
    margin-top: 6px;
    font-family: "Lato", sans-serif;
    font-size: 8px; letter-spacing: 3px; text-transform: uppercase;
    color: var(--blush);
  }
  .brand__est {
    margin-top: 4px;
    font-family: "Cormorant SC", serif;
    font-size: 13px; letter-spacing: 1px;
    color: var(--blush);
  }

  /* contact block */
  .contact {
    position: absolute; right: 30px; top: 36px;
    text-align: right;
  }
  .contact__person {
    font-family: "Cormorant SC", serif;
    font-size: 24px; font-weight: 500; letter-spacing: 1px;
    color: var(--blush);
  }
  .contact__line {
    font-family: "Lato", sans-serif;
    font-size: 13px; margin-top: 4px;
  }
  .contact__phone { font-size: 16px; letter-spacing: 0.5px; }
  .card--light .contact__line { color: var(--ink); }
  .card--dark .contact__line { color: var(--light-text); }

  /* backs */
  .pattern-field {
    position: absolute; inset: 0;
  }
  .card--light .pattern-field {
    background: linear-gradient(135deg, var(--blush-pale) 0%, var(--blush-soft) 50%, var(--blush-pale) 100%);
  }
  .card--dark .pattern-field {
    background: linear-gradient(135deg, #101010 0%, #1b1b1b 50%, #101010 100%);
  }
  .back-brand {
    position: absolute; left: 50%; top: 50%;
    transform: translate(-50%, -50%);
    display: flex; align-items: center; gap: 12px;
    padding: 18px 26px;
  }
  .card--light .back-brand { background: var(--paper); }
  .card--dark .back-brand { background: var(--night); }
  .back-brand__mark {
    width: 18px; height: 18px; border-radius: 50%;
  }
  .card--light .back-brand__mark { background: var(--ink); }
  .card--dark .back-brand__mark { background: var(--blush); }
  .back-brand__name {
    font-family: "Cinzel", serif;
    font-size: 26px; letter-spacing: 4px;
  }
  .card--light .back-brand__name { color: var(--ink); }
  .card--dark .back-brand__name { color: var(--blush); }
</style>
</head>
<body>
<main class="sheet">

  <!-- light front -->
  <section class="card card--light card--front-light">
    <div class="swirl-field" role="img" aria-label="Soft pink decorative swirl and rosebud ornament pattern"></div>
    <div class="brand">
      <span class="brand__mark"></span>
      <div class="brand__name">MARTA BELLE</div>
      <div class="brand__tagline">Designs &amp; Events</div>
      <div class="brand__est">Est 1954</div>
    </div>
    <div class="contact">
      <div class="contact__person">Elena Hart</div>
      <div class="contact__line contact__phone">555-418-2763</div>
      <div class="contact__line">www.martabelleevents-sample.com</div>
    </div>
  </section>

  <!-- light back -->
  <section class="card card--light card--back-light">
    <div class="pattern-field" role="img" aria-label="Faint pink repeating monogram and swirl pattern"></div>
    <div class="back-brand">
      <span class="back-brand__mark"></span>
      <span class="back-brand__name">MARTA BELLE</span>
    </div>
  </section>

  <!-- dark front -->
  <section class="card card--dark card--front-dark">
    <div class="swirl-field" role="img" aria-label="Dark grey decorative swirl and rosebud ornament pattern"></div>
    <div class="brand">
      <span class="brand__mark"></span>
      <div class="brand__name">MARTA BELLE</div>
      <div class="brand__tagline">Designs &amp; Events</div>
      <div class="brand__est">Est 1954</div>
    </div>
    <div class="contact">
      <div class="contact__person">Elena Hart</div>
      <div class="contact__line contact__phone">555-418-2763</div>
      <div class="contact__line">www.martabelleevents-sample.com</div>
    </div>
  </section>

  <!-- dark back -->
  <section class="card card--dark card--back-dark">
    <div class="pattern-field" role="img" aria-label="Faint dark grey repeating monogram and swirl pattern"></div>
    <div class="back-brand">
      <span class="back-brand__mark"></span>
      <span class="back-brand__name">MARTA BELLE</span>
    </div>
  </section>

</main>
</body>
</html>
```